New homepage and Product page - Meadow Vy

Reason: I have narrowed it done to 3 designers and just need to get the designs revised

Industry/Entity Type

Product

```html
<!DOCTYPE html>
<html lang="en">
<head>
<meta charset="utf-8">
<title>Meadow Vy — Homepage</title>
<link rel="stylesheet" href="https://fonts.googleapis.com/css2?family=Montserrat:wght@300;400;500;600;700&family=Caveat:wght@400&display=swap">
<style>
  :root {
    --green-dark: #3b7d0b;
    --green-mid: #5aa30f;
    --green-light: #8fcc2a;
    --green-text: #3f8416;
    --lime: #b4e05a;
    --ink: #444444;
    --ink-soft: #666666;
    --panel: #efefed;
    --panel-line: #dcdcd8;
    --footer: #e8e5df;
    --footer-line: #c9c3b7;
    --olive: #4f5f2a;
    --badge-grey: #5b524b;
    --icon-grey: #a8a8a8;
  }
  * { box-sizing: border-box; margin: 0; padding: 0; }
  html, body { width: 1200px; height: 1031px; overflow: hidden; background: #ffffff; }
  body { font-family: "Montserrat", Arial, sans-serif; color: var(--ink); }
  .page {
    position: relative; width: 1164px; height: 1000px;
    transform: scale(1.03093); transform-origin: 0 0;
  }
  .abs { position: absolute; }
  .nowrap { white-space: nowrap; }

  /* header */
  .site-header { left: 0; top: 0; width: 1164px; height: 67px; background: linear-gradient(#ffffff, #f1f1f1); border-top: 3px solid var(--green-mid); z-index: 3; }
  .header-tab { left: 430px; top: 60px; z-index: 3; }
  .main-nav { left: 223px; top: 30px; display: flex; gap: 38px; font-size: 11.5px; font-weight: 500; color: #555; z-index: 4; }
  .brand { left: 490px; top: 26px; width: 190px; z-index: 4; display: flex; align-items: center; justify-content: center; gap: 8px; white-space: nowrap; }
  .brand-name { font-size: 24px; font-weight: 700; color: #1f6b3a; letter-spacing: 0.5px; line-height: 1; }
  .brand-dot { width: 14px; height: 14px; border-radius: 50%; background: var(--green-light); }
  .phone { left: 802px; top: 25px; font-size: 18.5px; font-weight: 400; color: #555; z-index: 4; white-space: nowrap; }

  /* hero */
  .hero { left: 0; top: 67px; width: 1164px; height: 374px; background: radial-gradient(ellipse 420px 300px at 640px 220px, #86c823 0%, #5aa30f 55%, #3f8608 100%); overflow: hidden; }
  .hero-tagline { left: 0; top: 103px; width: 1164px; text-align: center; font-size: 12.5px; font-weight: 500; color: var(--lime); letter-spacing: 0.3px; z-index: 2; }
  .hero-title { left: 223px; top: 162px; font-size: 34px; font-weight: 300; color: #fff; letter-spacing: 0.3px; z-index: 2; white-space: nowrap; }
  .hero-copy { left: 223px; top: 220px; font-size: 12.2px; font-weight: 600; line-height: 17.8px; color: #fff; z-index: 2; white-space: nowrap; }
  .btn-learn { left: 224px; top: 338px; width: 131px; height: 37px; border: 2px solid #fff; border-radius: 4px; background: var(--olive); color: #fff; font-size: 13px; font-weight: 400; display: flex; align-items: center; justify-content: center; gap: 10px; z-index: 2; white-space: nowrap; }
  .btn-learn .chev { color: var(--lime); font-weight: 700; }
  .hero-script { left: 369px; top: 333px; font-family: "Caveat", cursive; font-size: 31px; color: var(--lime); z-index: 2; white-space: nowrap; }
  .hero-beans { left: 575px; top: 158px; width: 150px; height: 230px; border-radius: 50% 40% 45% 50%; background: radial-gradient(ellipse at 55% 50%, #6f8f2e 0%, #86b535 50%, rgba(120,190,40,0) 75%); z-index: 1; }
  .hero-pack { left: 708px; top: 131px; width: 211px; height: 270px; background: linear-gradient(#ffffff 0%, #f4f4f4 35%, #1f7a3a 36%, #1f7a3a 42%, #f4c51f 43%, #f4c51f 55%, #2f8a30 56%, #2f8a30 92%, #f2f2f2 93%); border: 1px solid #d8d8d8; z-index: 2; }
  .slider-arrow { top: 232px; width: 37px; height: 36px; background: #7ebf2a; color: #2f5f08; font-size: 15px; font-weight: 700; display: flex; align-items: center; justify-content: center; z-index: 2; }
  .slider-arrow.prev { left: 0; border-radius: 0 4px 4px 0; }
  .slider-arrow.next { left: 1127px; border-radius: 4px 0 0 4px; }
  .hero-notch { left: 500px; top: 426px; z-index: 3; }
  .slider-dots { left: 562px; top: 435px; display: flex; gap: 4px; z-index: 4; }
  .slider-dots span { width: 10px; height: 4px; border-radius: 2px; background: #dcdcdc; }
  .slider-dots span.active { background: var(--green-mid); }

  /* intro */
  .intro-title { left: 0; top: 478px; width: 1164px; text-align: center; font-size: 28.5px; font-weight: 300; color: var(--green-text); letter-spacing: 0.3px; white-space: nowrap; }
  .intro-copy { left: 0; top: 516px; width: 1164px; text-align: center; font-size: 15px; line-height: 24px; color: #555; white-space: nowrap; }

  /* products panel */
  .features { left: 224px; top: 597px; width: 715px; height: 201px; background: linear-gradient(90deg, #f7f7f6, var(--panel)); border: 1px solid var(--panel-line); }
  .features-bar { left: 224px; top: 597px; width: 430px; height: 30px; background: var(--green-dark); color: #fff; font-size: 14.5px; font-weight: 400; padding: 6px 0 0 17px; white-space: nowrap; }
  .feature { left: 240px; }
  .feature h3 { display: flex; align-items: center; gap: 4px; font-size: 12.3px; font-weight: 600; color: var(--ink); white-space: nowrap; }
  .feature p { margin-left: 24px; margin-top: 3px; font-size: 10.4px; line-height: 16.5px; color: var(--ink-soft); white-space: nowrap; }
  .feature-photo { left: 612px; top: 578px; width: 180px; height: 220px; border-radius: 45% 45% 0 0; background: linear-gradient(#f0dcc4 0%, #f6d3c2 55%, #fbd2c8 100%); }
  .guarantee-badge { left: 745px; top: 619px; }
  .guarantee-copy { left: 830px; top: 626px; width: 91px; text-align: right; font-size: 10.4px; font-weight: 600; line-height: 16.8px; color: #555; white-space: nowrap; }
  .guarantee-note { left: 780px; top: 709px; width: 141px; text-align: right; font-size: 10.4px; line-height: 16.8px; color: var(--ink-soft); white-space: nowrap; }

  /* trust row */
  .trust-icon { top: 826px; }
  .trust-text { font-size: 9.6px; line-height: 15px; color: var(--ink-soft); white-space: nowrap; }
  .trust-text strong { display: block; font-weight: 600; color: var(--ink); font-size: 10.2px; }
  .trust-text .more { color: var(--green-mid); font-weight: 600; }

  /* footer */
  .site-footer { left: 0; top: 903px; width: 1164px; height: 97px; background: var(--footer); border-top: 2px solid var(--footer-line); }
  .copyright { left: 224px; top: 926px; font-size: 8.5px; line-height: 16px; color: #777; white-space: nowrap; }
  .footer-nav { left: 705px; top: 930px; font-size: 8.5px; font-weight: 500; color: var(--green-mid); white-space: nowrap; }
  .footer-nav .sep { color: #999; margin: 0 3px; }
  .social { top: 925px; width: 22px; height: 22px; border-radius: 3px; background: var(--icon-grey); }
</style>
</head>
<body>
<div class="page">

  <div class="abs hero"></div>
  <div class="abs hero-tagline">A BRAND YOU CAN TRUST</div>
  <h1 class="abs hero-title">GREEN COFFEE BEAN</h1>
  <p class="abs hero-copy">Meadow Vy Green Coffee Bean is made with 100%<br>pure natural ingredients. Unlike other products,<br>Meadow Vy Green Coffee Bean is made with premium<br>green coffee bean that supplies 45% chlorogenic acid,<br>which is the active weight-loss component of green coffee bean.</p>
  <div class="abs btn-learn">LEARN MORE <span class="chev">❯</span></div>
  <div class="abs hero-script">Effective Weight Loss</div>
  <div class="abs hero-beans" role="img" aria-label="Green coffee beans and leaves"></div>
  <div class="abs hero-pack" role="img" aria-label="Green Coffee Bean two bottle bonus pack box"></div>
  <div class="abs slider-arrow prev">❮</div>
  <div class="abs slider-arrow next">❯</div>
  <svg class="abs hero-notch" width="164" height="16" viewBox="0 0 164 16" aria-hidden="true">
    <path d="M0 16 C30 16 40 2 82 2 C124 2 134 16 164 16 Z" fill="#ffffff"/>
  </svg>
  <div class="abs slider-dots"><span class="active"></span><span></span><span></span></div>

  <header class="abs site-header"></header>
  <svg class="abs header-tab" width="310" height="32" viewBox="0 0 310 32" aria-hidden="true">
    <path d="M0 0 C40 0 50 28 110 28 L200 28 C260 28 270 0 310 0 Z" fill="#f1f1f1"/>
  </svg>
  <nav class="abs main-nav"><span>Home</span><span>Products</span><span>Contact Us</span></nav>
  <div class="abs brand"><span class="brand-name">MEADOW VY</span><span class="brand-dot"></span></div>
  <div class="abs phone">1 800 555 0142</div>

  <h2 class="abs intro-title">THE BEST OF NATURE &amp; SCIENCE</h2>
  <p class="abs intro-copy">New Meadow Vy is line of natural, high-quality, weight-loss supplements that are<br>scientifically formulated for better efficiency!</p>

  <section class="abs features"></section>
  <div class="abs features-bar">ALL OUR PRODUCTS ARE</div>
  <div class="abs feature" style="top:643px">
    <h3><svg width="20" height="20" viewBox="0 0 20 20" aria-hidden="true"><path d="M2 18 C2 8 8 3 18 2 C17 12 12 17 2 18 Z" fill="#6db52a"/></svg>100% PURE NATURAL INGREDIENTS</h3>
    <p>Meadow Vy products are made with 100% pure natural<br>ingredients. Unlike other products, Meadow Vy products<br>are made with premium natural ingredients for effective results.</p>
  </div>
  <div class="abs feature" style="top:725px">
    <h3><svg width="20" height="20" viewBox="0 0 20 20" aria-hidden="true"><path d="M2 18 C2 8 8 3 18 2 C17 12 12 17 2 18 Z" fill="#6db52a"/></svg>SCIENTIFICALLY FORMULATED</h3>
    <p>Meadow Vy products are scientifically formulated to deliver<br>the exact clinically tested doses that are needed to see results!</p>
  </div>
  <div class="abs feature-photo" role="img" aria-label="Portrait photo of a smiling woman"></div>
  <svg class="abs guarantee-badge" width="82" height="82" viewBox="0 0 82 82" aria-hidden="true">
    <circle cx="41" cy="41" r="39" fill="#f7c600"/>
    <circle cx="41" cy="41" r="31" fill="#f0a800"/>
  </svg>
  <div class="abs guarantee-copy">Meadow Vy is<br>guaranteed to<br>work or your<br>money back</div>
  <div class="abs guarantee-note">Simply return it to the<br>place of purchase within<br>30 days for a refund<br>with original receipt</div>

  <svg class="abs trust-icon" style="left:223px" width="53" height="53" viewBox="0 0 53 53" aria-hidden="true">
    <circle cx="26.5" cy="26.5" r="26" fill="var(--badge-grey)"/>
  </svg>
  <p class="abs trust-text" style="left:288px; top:830px">Lorem ipsum dolor sit amet, consectetur adipisicing elit, sed<br>do eiusmod incididunt ut labore et dolore magna aliqua<br>enim ad minim laboris nisi ut aliquip ext ... <span class="more">Find out more</span></p>
  <svg class="abs trust-icon" style="left:597px; top:829px" width="51" height="50" viewBox="0 0 51 50" aria-hidden="true">
    <path d="M2 2 L49 2 L49 26 C49 38 36 45 25.5 49 C15 45 2 38 2 26 Z" fill="#8f8f8f"/>
  </svg>
  <p class="abs trust-text" style="left:659px; top:828px"><strong>Made in the USA</strong>Meadow Vy is manufactured in a GMP-compliant<br>manufacturing facility to ensure 100% quality.</p>

  <footer class="abs site-footer"></footer>
  <div class="abs copyright">© Copyright 2014 Meadow Vy</div>
  <nav class="abs footer-nav">Home<span class="sep">|</span>Products<span class="sep">|</span>Contact Us</nav>
  <div class="abs social" style="left:858px"></div>
  <div class="abs social" style="left:888px"></div>
  <div class="abs social" style="left:918px"></div>

</div>
</body>
</html>
```